The Quiet Hour Safeguard Handbook

A book cover. The book will be marketed as a promotional item for financial advisors, financial planners, independent insurance agents, bankers, and any professional who views their role as guardian of their clients assets and helping them manage risk.

```html
<!DOCTYPE html>
<html lang="en">
<head>
<meta charset="utf-8">
<title>The Quiet Hour Safeguard Handbook</title>
<link rel="stylesheet" href="https://fonts.googleapis.com/css2?family=Bebas+Neue&family=Nunito:wght@400;500&display=swap">
<style>
  :root {
    --backdrop: #e9e7e3;
    --paper: #fbfbfb;
    --navy: #13305f;
    --navy-deep: #0f2449;
    --mist: #c9d4e4;
    --haze: #8ea2c2;
    --gold: #d8a72c;
    --ink: #1a1a1a;
    --white: #ffffff;
  }
  * { margin: 0; padding: 0; box-sizing: border-box; }
  html, body {
    width: 1006px;
    height: 1200px;
    overflow: hidden;
    background: var(--backdrop);
  }
  .cover {
    position: absolute;
    left: 95px;
    top: 0;
    width: 816px;
    height: 1200px;
    background: linear-gradient(180deg, var(--white) 0%, var(--paper) 45%, #eef1f5 100%);
    overflow: hidden;
  }
  .title {
    position: absolute;
    left: 0;
    right: 0;
    top: 100px;
    text-align: center;
    font-family: "Bebas Neue", "Oswald", sans-serif;
    color: var(--navy);
    line-height: 0.95;
    letter-spacing: 1px;
  }
  .title-main { display: block; font-size: 150px; }
  .title-sub { display: block; font-size: 92px; margin-top: 8px; }
  .subtitle {
    position: absolute;
    left: 0;
    right: 0;
    top: 355px;
    text-align: center;
    font-family: "Nunito", sans-serif;
    font-weight: 500;
    font-size: 24px;
    color: var(--ink);
  }
  .scene {
    position: absolute;
    left: 0;
    top: 500px;
    width: 816px;
    height: 510px;
    background:
      radial-gradient(ellipse 120px 150px at 50% 55%, #f6e4b0 0%, rgba(246,228,176,0) 100%),
      linear-gradient(180deg, rgba(255,255,255,0) 0%, var(--mist) 35%, var(--haze) 60%, var(--navy) 100%);
  }
  .icon-column {
    position: absolute;
    top: 520px;
    display: flex;
    flex-direction: column;
    gap: 30px;
  }
  .icon-column.left { left: 128px; }
  .icon-column.right { left: 648px; }
  .icon { width: 44px; height: 44px; display: block; }
  .icon * { fill: none; stroke: var(--navy); stroke-width: 2; stroke-linecap: round; stroke-linejoin: round; }
  .band {
    position: absolute;
    left: 0;
    top: 1010px;
    width: 816px;
    height: 190px;
    background: var(--navy-deep);
    border-top: 3px solid var(--gold);
  }
  .tagline {
    position: absolute;
    left: 0;
    right: 0;
    top: 55px;
    text-align: center;
    font-family: "Nunito", sans-serif;
    font-size: 22px;
    line-height: 1.6;
    color: var(--white);
  }
</style>
</head>
<body>
  <main class="cover">
    <h1 class="title">
      <span class="title-main">The Quiet Hour</span>
      <span class="title-sub">Safeguard Handbook</span>
    </h1>
    <p class="subtitle">protect yourself and your family in the AI Age</p>

    <div class="scene" role="img" aria-label="Illustration of a family silhouette holding hands inside a shield, on a winding path through blue hills with a city skyline"></div>

    <div class="icon-column left">
      <svg class="icon" viewBox="0 0 44 44"><rect x="6" y="11" width="32" height="22" rx="3"/><line x1="6" y1="18" x2="38" y2="18"/><line x1="11" y1="26" x2="20" y2="26"/></svg>
      <svg class="icon" viewBox="0 0 44 44"><circle cx="22" cy="22" r="18"/><circle cx="22" cy="18" r="6"/><path d="M12 33c2-6 6-8 10-8s8 2 10 8"/></svg>
      <svg class="icon" viewBox="0 0 44 44"><rect x="10" y="19" width="24" height="19" rx="2"/><path d="M15 19v-5a7 7 0 0 1 14 0v5"/><circle cx="22" cy="28" r="2"/></svg>
      <svg class="icon" viewBox="0 0 44 44"><rect x="6" y="11" width="32" height="22" rx="1"/><path d="M6 11l16 13 16-13"/></svg>
    </div>

    <div class="icon-column right">
      <svg class="icon" viewBox="0 0 44 44"><rect x="9" y="10" width="26" height="18" rx="2"/><path d="M5 33h34"/></svg>
      <svg class="icon" viewBox="0 0 44 44"><path d="M8 18a20 20 0 0 1 28 0"/><path d="M13 24a12 12 0 0 1 18 0"/><circle cx="22" cy="30" r="2"/></svg>
      <svg class="icon" viewBox="0 0 44 44"><path d="M14 34c-2-4-3-8-3-12a11 11 0 0 1 22 0"/><path d="M18 36c-1-4-2-9-2-14a6 6 0 0 1 12 0c0 5 1 9 2 12"/><path d="M22 22c0 5 1 10 3 14"/></svg>
      <svg class="icon" viewBox="0 0 44 44"><path d="M6 16l16-9 16 9z"/><line x1="11" y1="19" x2="11" y2="32"/><line x1="18" y1="19" x2="18" y2="32"/><line x1="26" y1="19" x2="26" y2="32"/><line x1="33" y1="19" x2="33" y2="32"/><line x1="6" y1="36" x2="38" y2="36"/></svg>
    </div>

    <footer class="band">
      <p class="tagline">it's better to have it and not need it<br>than need it and not have it</p>
    </footer>
  </main>
</body>
</html>
```